Need a graphic design for front page of tech blog

Hi,

So I'm looking to start a project of redesigning the front homepage for all of my tech sites. I already have a developer that will code the change, so what I need from someone here is to give me a graphic design, which I can then give to my developers to code.

Currently, I have the plain old boring default list of WordPress posts as the front page, which needs to be replaced with something a little more like a magazine or newspaper style. You can see my four sites here:

https://www.quill-gadget-notes.com/
https://servicebenchnerd.com/
https://theatticbitworks.com/
https://www.hoppingtolark.com/

I've attached some screenshots of mobile sites that I like in terms of look and style. Some desktop sites that I like are here (I like some parts more than others, I've attached screenshots of the sections I like):

https://www.ploddernook.com/
https://www.gizmonest.com/
https://www.pinewirebulletin.com/
https://www.takeholdwith.com/
https://www.dayspool.com/

Basically, I don't need all that text after each post. Seems like most sites now just have an image, a title, the author and date info and possibly the category.

Right now I'm only showing 10 posts and one has to scroll through lots of text to see them all. The sidebar is good, but I think we can get rid of that for the front page and instead have different sections like Latest Tips, and then some section headers based on the categories.

Anyway, I'm looking for someone who can come up with multiple designs, so that I have some choice.

I'm looking to get this done over the next few weeks. Also, please include in your price the cost of any revisions and how many revisions can be done.

Thanks

Tarun

```html
<!DOCTYPE html>
<html lang="en">
<head>
<meta charset="utf-8">
<title>Tech Blog Front Page</title>
<link href="https://fonts.googleapis.com/css2?family=Roboto:wght@400;500;700&display=swap" rel="stylesheet">
<style>
:root{
  --blue:#3296f5;
  --blue-line:#6db2f5;
  --ink:#141414;
  --text:#2a2a2a;
  --meta:#a9cff5;
  --white:#ffffff;
  --divider:#9fcaf3;
}
*{box-sizing:border-box;margin:0;padding:0}
html,body{width:1200px;height:2222px;overflow:hidden;background:var(--white)}
body{position:relative;font-family:'Roboto',sans-serif;color:var(--text)}

/* header */
.site-header .logo{position:absolute;left:76px;top:12px;width:241px;height:40px;border:1px solid var(--blue-line);display:flex;align-items:center;justify-content:center;color:var(--blue);font-size:13px;letter-spacing:.5px}
.site-header .search{position:absolute;left:465px;top:14px;width:267px;height:25px;border-bottom:1px solid var(--blue-line)}
.site-header .search svg{position:absolute;right:0;top:2px}
.site-header .menu{position:absolute;left:1097px;top:22px}

/* sections */
.post-section{position:absolute;left:0;width:1200px}
.section-head{position:relative;height:60px;display:flex;align-items:center;justify-content:center}
.section-head .rule{width:59px;height:1px;background:var(--ink);margin-right:15px;margin-top:18px}
.section-head h2{font-size:44px;font-weight:700;color:var(--ink);letter-spacing:.2px}
.see-more{position:absolute;left:1035px;top:22px;display:flex;align-items:center;gap:12px;color:var(--blue);font-size:11px;text-decoration:none}

.featured{top:114px}
.recent{top:650px}
.trending{top:1140px}
.featured .card-grid{margin-top:56px;--thumb:188px}
.recent .card-grid{margin-top:74px;--thumb:136px}
.trending .card-grid{margin-top:70px;--thumb:186px}

.card-grid{margin-left:76px;width:1045px;display:grid;grid-template-columns:repeat(4,1fr);column-gap:20px}
.post-card{position:relative;text-align:center}
.post-card.is-active::before{content:"";position:absolute;left:-7px;top:88px;width:260px;height:246px;border:1px solid var(--blue-line);z-index:0}
.thumb{position:relative;z-index:1;height:var(--thumb);width:100%}
.faded .thumb{opacity:.55}
.meta{position:relative;z-index:1;display:flex;justify-content:space-between;align-items:center;margin-top:12px;font-size:9px;color:var(--meta)}
.meta .author{display:flex;align-items:center;gap:5px}
.meta .avatar{width:14px;height:14px;border-radius:50%;background:#5b6470}
.post-card h3{position:relative;z-index:1;margin:18px auto 0;width:210px;height:40px;font-size:13px;font-weight:400;line-height:18px;color:var(--ink)}
.tag{position:relative;z-index:1;display:inline-block;margin-top:14px;width:137px;height:24px;line-height:22px;border:1px solid var(--blue);border-radius:12px;color:var(--blue);font-size:11px;text-decoration:none}

/* thumbnail placeholders */
.t-film{background:linear-gradient(120deg,#8d8fb4,#c9a48a 45%,#6fb6e6)}
.t-chat{background:linear-gradient(135deg,#8fd3dc,#b7e2e6 50%,#f29a6e)}
.t-desk{background:linear-gradient(180deg,#cfcfcf,#b79a7b 60%,#c8c3bd)}
.t-keys{background:linear-gradient(150deg,#d9dde5,#7b8ca5 60%,#a6b2c4)}
.t-phone{background:linear-gradient(120deg,#6c7075,#d6cdc6 55%,#f0ece8)}
.t-laptop{background:linear-gradient(160deg,#a7a7a7,#6c6c6c 55%,#3e3e3e)}
.t-eye{background:linear-gradient(135deg,#6a5e52,#8a9aa3 50%,#7a6a5c)}

/* subscribe */
.subscribe{position:absolute;left:0;top:1698px;width:1200px;height:232px;background:var(--blue);color:var(--white)}
.subscribe .section-head{position:absolute;left:0;top:36px;width:1200px}
.subscribe .section-head .rule{background:var(--white)}
.subscribe .section-head h2{color:var(--white);font-weight:500}
.subscribe-form .email{position:absolute;left:387px;top:146px;width:376px;height:24px;border-bottom:1px solid var(--white);font-size:13px;color:var(--white)}
.subscribe-form .submit{position:absolute;left:801px;top:145px;display:flex;align-items:center;gap:12px;font-size:15px;color:var(--ink)}

/* footer */
.site-footer{position:absolute;left:0;top:1979px;width:1200px;height:196px}
.footer-col{position:absolute;top:0;height:196px;text-align:center}
.footer-col h4{margin-top:8px;font-size:16px;font-weight:400;color:var(--ink)}
.footer-col ul{list-style:none;margin-top:25px}
.footer-col li{height:28px;font-size:13px;color:var(--blue)}
.col-main{left:0;width:385px;border-right:1px solid var(--divider)}
.col-other{left:385px;width:428px;border-right:1px solid var(--divider)}
.col-social{left:813px;width:387px}
.social-links{display:flex;justify-content:center;gap:22px;margin-top:38px;list-style:none}
.social-links li{font-size:13px;font-weight:500;color:var(--blue)}
</style>
</head>
<body>

<header class="site-header">
  <div class="logo">LOGO</div>
  <div class="search">
    <svg width="18" height="18" viewBox="0 0 18 18" fill="none" stroke="#3296f5" stroke-width="1.2"><circle cx="11" cy="7" r="5"/><line x1="7.5" y1="10.5" x2="2" y2="16"/></svg>
  </div>
  <svg class="menu" width="26" height="16" viewBox="0 0 26 16" stroke="#3296f5" stroke-width="1.4"><line x1="4" y1="2" x2="26" y2="2"/><line x1="0" y1="14" x2="26" y2="14"/></svg>
</header>

<section class="post-section featured">
  <div class="section-head"><span class="rule"></span><h2>Featured</h2>
    <a class="see-more" href="#">See more <svg width="32" height="14" viewBox="0 0 32 14" fill="none" stroke="#3296f5" stroke-width="1.2"><line x1="0" y1="7" x2="31" y2="7"/><polyline points="24,1 31,7 24,13"/></svg></a></div>
  <div class="card-grid">
    <article class="post-card"><div class="thumb t-film" role="img" aria-label="Film strip with sunset frames"></div><div class="meta"><span>27.02.2019</span><span class="author">By Milo Varrek <i class="avatar"></i></span></div><h3>How to Record Professional Quality Video on Your PocketOne</h3><a class="tag" href="#">PocketOne</a></article>
    <article class="post-card is-active"><div class="thumb t-chat" role="img" aria-label="Illustration of team chat on a phone"></div><div class="meta"><span>27.02.2019</span><span class="author">By Milo Varrek <i class="avatar"></i></span></div><h3>Best Free Team Chat Software for Paneos 10</h3><a class="tag" href="#">Tools Review</a></article>
    <article class="post-card"><div class="thumb t-desk" role="img" aria-label="Desktop computer and keyboard on a wooden desk"></div><div class="meta"><span>27.02.2019</span><span class="author">By Milo Varrek <i class="avatar"></i></span></div><h3>The Best Orchard OS Keyboard Shortcuts</h3><a class="tag" href="#">Paneos 10</a></article>
    <article class="post-card"><div class="thumb t-keys" role="img" aria-label="Snail on a laptop keyboard"></div><div class="meta"><span>27.02.2019</span><span class="author">By Milo Varrek <i class="avatar"></i></span></div><h3>How to Fix a Slow OrchardBook in 5 Easy Ways</h3><a class="tag" href="#">Uncategorized</a></article>
  </div>
</section>

<section class="post-section recent">
  <div class="section-head"><span class="rule"></span><h2>Recent</h2>
    <a class="see-more" href="#">See more <svg width="32" height="14" viewBox="0 0 32 14" fill="none" stroke="#3296f5" stroke-width="1.2"><line x1="0" y1="7" x2="31" y2="7"/><polyline points="24,1 31,7 24,13"/></svg></a></div>
  <div class="card-grid faded">
    <article class="post-card"><div class="thumb t-phone" role="img" aria-label="Hand holding a phone with passcode screen"></div><div class="meta"><span>27.02.2019</span><span class="author">By Milo Varrek <i class="avatar"></i></span></div><h3>How To Make Your PocketOS Passcode Longer In Case The Cops...</h3><a class="tag" href="#">PocketOS</a></article>
    <article class="post-card"><div class="thumb t-laptop" role="img" aria-label="Laptop on a dark table"></div><div class="meta"><span>27.02.2019</span><span class="author">By Milo Varrek <i class="avatar"></i></span></div><h3>Best Free Team Chat Software for Paneos 10</h3><a class="tag" href="#">Paneos 10</a></article>
    <article class="post-card"><div class="thumb t-eye" role="img" aria-label="Close-up photograph with colourful reflection"></div><div class="meta"><span>27.02.2019</span><span class="author">By Milo Varrek <i class="avatar"></i></span></div><h3>Best Free Team Chat Software for Paneos 10</h3><a class="tag" href="#">Tools Review</a></article>
    <article class="post-card"><div class="thumb t-chat" role="img" aria-label="Illustration of team chat on a phone"></div><div class="meta"><span>27.02.2019</span><span class="author">By Milo Varrek <i class="avatar"></i></span></div><h3>Best Free Team Chat Software for Paneos 10</h3><a class="tag" href="#">Tools Review</a></article>
  </div>
</section>

<section class="post-section trending">
  <div class="section-head"><span class="rule"></span><h2>Trending</h2>
    <a class="see-more" href="#">See more <svg width="32" height="14" viewBox="0 0 32 14" fill="none" stroke="#3296f5" stroke-width="1.2"><line x1="0" y1="7" x2="31" y2="7"/><polyline points="24,1 31,7 24,13"/></svg></a></div>
  <div class="card-grid faded">
    <article class="post-card"><div class="thumb t-film" role="img" aria-label="Film strip with sunset frames"></div><div class="meta"><span>27.02.2019</span><span class="author">By Milo Varrek <i class="avatar"></i></span></div><h3>How to Record Professional Quality Video on Your PocketOne</h3><a class="tag" href="#">PocketOne</a></article>
    <article class="post-card"><div class="thumb t-chat" role="img" aria-label="Illustration of team chat on a phone"></div><div class="meta"><span>27.02.2019</span><span class="author">By Milo Varrek <i class="avatar"></i></span></div><h3>Best Free Team Chat Software for Paneos 10</h3><a class="tag" href="#">Tools Review</a></article>
    <article class="post-card"><div class="thumb t-desk" role="img" aria-label="Desktop computer and keyboard on a wooden desk"></div><div class="meta"><span>27.02.2019</span><span class="author">By Milo Varrek <i class="avatar"></i></span></div><h3>The Best Orchard OS Keyboard Shortcuts</h3><a class="tag" href="#">Paneos 10</a></article>
    <article class="post-card"><div class="thumb t-keys" role="img" aria-label="Snail on a laptop keyboard"></div><div class="meta"><span>27.02.2019</span><span class="author">By Milo Varrek <i class="avatar"></i></span></div><h3>How to Fix a Slow OrchardBook in 5 Easy Ways</h3><a class="tag" href="#">Uncategorized</a></article>
  </div>
</section>

<section class="subscribe">
  <div class="section-head"><span class="rule"></span><h2>Subscribe</h2></div>
  <form class="subscribe-form">
    <div class="email">Email Address</div>
    <div class="submit">Subscribe <svg width="30" height="14" viewBox="0 0 30 14" fill="none" stroke="#141414" stroke-width="1.3"><line x1="0" y1="7" x2="29" y2="7"/><polyline points="22,1 29,7 22,13"/></svg></div>
  </form>
</section>

<footer class="site-footer">
  <div class="footer-col col-main"><h4>Main Sections</h4><ul><li>Featured</li><li>Recent</li><li>Trending</li><li>Suscribe</li></ul></div>
  <div class="footer-col col-other"><h4>Other</h4><ul><li>About</li><li>Contact</li><li>Privacy Policy</li></ul></div>
  <div class="footer-col col-social"><h4>Find us here:</h4><ul class="social-links"><li>Pixmosaic</li><li>Chatterly</li><li>Circlebook</li></ul></div>
</footer>

</body>
</html>
```